Velmora Limited Business Card Design Project

Velmora Limited is my UK based company used as my brand to work as an Interim Manager or contractor in project/programme management and Non-Executive Director.

Velmora is Latin for 'execute' as in getting things done rather than killing people!

Logo and design needs to promote reliable, professional, and successful project delivery. Simple, elegant, clean, professional are words that should spring to mind!
Updates

Target Market(s)

Middle and senior management in english speaking countries aged 35 - 60 that hire and task qualified and experienced project/programme managers and Non-Executive Directors.

Industry/Entity Type

Contractor

Font styles to use
Serif
Sans Serif

Requirements
Must have
• Mobile telephone number 07840 512697
email address peterhalloway@velmora.co.uk
Nice to have
• Linkwell link to my profile.

Interim Manager
Should not have
• avoid Ticks and clocks

```html
<!DOCTYPE html>
<html lang="en">
<head>
<meta charset="utf-8">
<title>Velmora Limited – Business Card</title>
<link rel="stylesheet" href="https://fonts.googleapis.com/css2?family=Lato:wght@300;400;900&family=Russo+One&display=swap">
<style>
  :root {
    --stage: #e6e6e4;
    --card: #1b3438;
    --gold: #dba02a;
    --ink-light: #f2f2ee;
    --muted-line: #c9ccc8;
    --decor: #2c474b;
  }
  * { box-sizing: border-box; margin: 0; padding: 0; }
  html, body { width: 1200px; height: 1000px; overflow: hidden; }
  body {
    background: var(--stage);
    font-family: "Lato", Arial, sans-serif;
    position: relative;
  }
  .business-card {
    position: absolute;
    left: 100px; top: 215px;
    width: 1000px; height: 570px;
    background: var(--card);
    overflow: hidden;
  }
  .brand {
    position: absolute;
    left: 78px; top: 92px;
    display: flex; align-items: center; gap: 18px;
  }
  .brand-mark {
    width: 26px; height: 26px;
    background: var(--ink-light);
    border-radius: 50%;
  }
  .brand-name {
    font-family: "Lato", Arial, sans-serif;
    font-weight: 900;
    color: var(--gold);
    font-size: 64px;
    line-height: 1.02;
    letter-spacing: 2px;
    text-transform: uppercase;
  }
  .brand-name span { display: block; }
  .decor-field {
    position: absolute;
    left: 220px; top: 300px;
    width: 360px; height: 210px;
    background: radial-gradient(ellipse at center, #3a4a3e 0%, var(--decor) 55%, var(--card) 100%);
    opacity: 0.55;
    border-radius: 8px;
  }
  .contact-block {
    position: absolute;
    right: 78px; top: 90px;
    text-align: right;
    color: var(--ink-light);
  }
  .person-name {
    font-family: "Russo One", Arial, sans-serif;
    color: var(--gold);
    font-size: 32px;
    letter-spacing: 1px;
    line-height: 1;
  }
  .person-role {
    font-size: 28px;
    font-weight: 400;
    margin-top: 2px;
  }
  .contact-list { list-style: none; margin-top: 30px; }
  .contact-list li {
    display: flex; justify-content: flex-end; align-items: center;
    gap: 14px;
    font-size: 26px;
    font-weight: 400;
    letter-spacing: 0.3px;
    height: 44px;
  }
  .contact-icon { width: 28px; height: 28px; flex: none; }
  .contact-icon.square {
    background: var(--gold);
    width: 24px; height: 24px;
    border-radius: 3px;
    margin: 0 2px;
  }
  .base-band {
    position: absolute;
    left: 0; bottom: 0;
    width: 100%; height: 30px;
    background: var(--gold);
  }
</style>
</head>
<body>
  <section class="business-card">
    <div class="brand">
      <div class="brand-mark"></div>
      <div class="brand-name"><span>Velmora</span><span>Limited</span></div>
    </div>

    <div class="decor-field" role="img" aria-label="Faint decorative brand motif"></div>

    <div class="contact-block">
      <p class="person-name">PETER HALLOWAY</p>
      <p class="person-role">Director</p>
      <ul class="contact-list">
        <li>07840 512697
          <svg class="contact-icon" viewBox="0 0 28 28" aria-hidden="true">
            <rect x="8" y="2" width="12" height="24" rx="2" fill="none" stroke="var(--gold)" stroke-width="2"/>
            <line x1="12" y1="22" x2="16" y2="22" stroke="var(--gold)" stroke-width="2"/>
          </svg>
        </li>
        <li>peterhalloway@velmora.co.uk
          <svg class="contact-icon" viewBox="0 0 28 28" aria-hidden="true">
            <rect x="2" y="7" width="24" height="15" fill="var(--gold)"/>
            <polyline points="2,7 14,16 26,7" fill="none" stroke="var(--card)" stroke-width="2"/>
          </svg>
        </li>
        <li>linkwell/peterhalloway
          <span class="contact-icon square" aria-hidden="true"></span>
        </li>
      </ul>
    </div>

    <div class="base-band"></div>
  </section>
</body>
</html>
```